TBranwell executive consulting

We need a basic clean website for executive consulting. Rosalind is the previos CIO for bluecrest airways and currently supports several technology companies with innovation and transformation.

Target Market(s)

C level technology and CIO training

Industry/Entity Type

Technology and travel industry

Coding

Coded - Design and coding required

Number of Pages Required

3 page

Font styles to use
Sans Serif

Colors
0054AA
0677BA
7BADD7
CADEEF
E8F1F8
0094D4
00A9DD
6FCCEA
C7EBF8
E9F6FB

Requirements
Must have
• Home page, about us, services social media links

```html
<!DOCTYPE html>
<html lang="en">
<head>
<meta charset="utf-8">
<title>TBranwell Executive Consulting</title>
<link rel="stylesheet" href="https://fonts.googleapis.com/css2?family=Poppins:wght@400;500;600&family=Oswald:wght@600&family=Libre+Caslon+Text&display=swap">
<style>
:root{
  --navy:#0054AA;
  --blue:#0677BA;
  --sky:#0094D4;
  --cyan:#00A9DD;
  --cyan-soft:#6FCCEA;
  --pale:#E8F1F8;
  --pale-2:#CADEEF;
  --ice:#E9F6FB;
  --ink:#1b1b1b;
  --text:#333;
  --dark:#1a1a1a;
  --star:#f39c12;
}
*{box-sizing:border-box;margin:0;padding:0}
html,body{width:1200px;height:3275px;overflow:hidden}
body{position:relative;font-family:"Poppins",sans-serif;color:var(--text);background:#fff}
.abs{position:absolute}
a{color:inherit;text-decoration:none}

/* top bar */
.topbar{left:0;top:0;width:1200px;height:41px;background:#f6f8fa;font-size:13px;color:#222}
.topbar .mail{left:141px;top:11px;display:flex;align-items:center;gap:7px}
.topbar .social{right:141px;top:11px;display:flex;align-items:center;gap:14px}
.dot-ic{width:20px;height:20px;border-radius:50%;background:var(--sky)}
.sq{width:13px;height:13px;border:2px solid var(--sky);border-radius:3px}

/* header */
.header{left:0;top:41px;width:1200px;height:105px;background:linear-gradient(90deg,#00aedd 0%,#0aa4d3 55%,#1a6788 100%);color:#fff}
.brand{font-size:30px;font-weight:500;letter-spacing:.5px;color:#fff}
.header .brand{left:141px;top:32px}
.nav{left:564px;top:44px;display:flex;gap:47px;font-size:14.5px}
.callbox{left:866px;top:27px;display:flex;align-items:center;gap:12px}
.callbox .ring{width:50px;height:50px;border:2px solid #fff;border-radius:50%;display:flex;align-items:center;justify-content:center}
.callbox .t{font-size:18px;line-height:25px;font-weight:500}

/* hero */
.hero{left:0;top:146px;width:1200px;height:490px;background:linear-gradient(90deg,#fff 0%,#f4f6f8 40%,#eef1f4 100%)}
.hero-photo{left:400px;top:0;width:800px;height:490px;clip-path:polygon(34% 0,100% 0,100% 100%,0 100%);background:linear-gradient(160deg,#e6e9ec 0%,#cfd4d9 45%,#8d939a 70%,#e9ecef 100%)}
.hero .kicker{left:143px;top:134px;font-family:"Libre Caslon Text",serif;font-size:29px;color:#222}
.hero h1{left:143px;top:177px;font-family:"Oswald",sans-serif;font-weight:600;font-size:48px;line-height:52px;color:#1a1a1a;letter-spacing:.3px}
.hero .call{left:141px;top:292px;display:flex;align-items:center;gap:16px}
.hero .call .ring{width:50px;height:50px;border:2px solid #222;border-radius:50%;display:flex;align-items:center;justify-content:center}
.hero .call .t{font-size:18px;line-height:25px;color:#222}

/* about */
.about-bg{left:0;top:724px;width:470px;height:528px;background:var(--pale)}
.about-frame{left:141px;top:784px;width:388px;height:421px;border-left:7px solid var(--sky);border-bottom:7px solid var(--sky)}
.about-photo{left:155px;top:784px;width:374px;height:409px;border-radius:0 90px 0 0;background:linear-gradient(135deg,#c9c2b8 0%,#8a7b6c 45%,#2d2a2e 100%)}
.about-badge{left:417px;top:1007px;width:177px;height:119px;background:var(--sky);border:4px solid #fff;border-radius:12px;color:#fff;text-align:center;padding-top:10px}
.about-badge b{display:block;font-size:40px;line-height:46px;font-weight:600}
.about-badge span{font-size:17px;line-height:22px}
.about-text{left:624px;top:760px;width:430px}
.about-text h2{font-size:34px;font-weight:600;color:#1b1b1b;letter-spacing:.5px}
.about-text h2 em{font-style:normal;font-size:23px;font-weight:500;color:var(--cyan);margin-right:10px}
.about-text .role{font-size:15px;line-height:23px;font-weight:500;color:#222;margin-top:2px}
.about-text p{font-size:14.5px;line-height:21.2px;margin-top:18px;color:#333}
.btn{display:inline-flex;align-items:center;gap:9px;background:var(--cyan);color:#fff;border-radius:22px;font-size:15px;font-weight:500;letter-spacing:.4px}
.about-text .btn{margin-top:20px;padding:10px 20px}

/* services */
.section-title{left:0;width:1200px;text-align:center;font-size:37px;font-weight:600;color:#222;letter-spacing:.5px}
.section-title em{font-style:normal;color:var(--cyan)}
.card{top:1412px;width:282px;height:370px;background:#fff;border-radius:12px;box-shadow:0 3px 14px rgba(0,0,0,.12);overflow:hidden}
.card .img{height:105px}
.card .icon{position:absolute;left:20px;top:86px;width:72px;height:72px;border-radius:50%;background:var(--cyan);border:4px solid #fff;display:flex;align-items:center;justify-content:center}
.card h3{position:absolute;left:18px;top:172px;width:250px;font-size:18px;line-height:22px;font-weight:500;color:#222}
.card ul{position:absolute;left:18px;list-style:none;width:250px}
.card li{position:relative;font-size:13px;line-height:19px;color:#333;margin-bottom:9px}
.card li:before{content:"";position:absolute;left:-19px;top:4px;border-left:8px solid var(--navy);border-top:6px solid transparent;border-bottom:6px solid transparent}
.card .more{position:absolute;left:18px;top:335px;font-size:13px;color:#222;letter-spacing:.4px}
.card .more b{color:var(--navy);margin-left:8px}

/* testimonials */
.tcard{top:2011px;width:430px;height:274px;background:#fff;box-shadow:0 3px 14px rgba(0,0,0,.1)}
.tcard.active .inner{position:absolute;left:8px;top:8px;right:8px;bottom:8px;background:var(--pale)}
.tcard p{position:absolute;left:38px;top:24px;width:360px;font-size:13px;line-height:23px;color:#222}
.tcard .name{position:absolute;left:38px;top:214px;font-size:15px;font-weight:500;color:#111}
.tcard .pos{position:absolute;left:38px;top:237px;font-size:12.5px;color:#333}
.tcard .stars{position:absolute;left:192px;top:233px;color:var(--star);font-size:12px;letter-spacing:1px}
.tcard .quote{position:absolute;right:24px;top:210px;font-size:60px;line-height:60px;font-family:Georgia,serif;color:var(--pale-2);font-weight:700}
.avatar{top:2266px;width:48px;height:48px;border-radius:50%;border:3px solid #fff;background:linear-gradient(135deg,#d8b8a0,#8c6a55)}
.arrow{width:42px;height:42px;border-radius:50%;display:flex;align-items:center;justify-content:center}
.dots span{position:absolute;width:14px;height:14px;border:1.5px solid var(--cyan);border-radius:50%;top:0}

/* contact */
.footer-bg{left:0;top:2761px;width:1200px;height:474px;background:var(--dark)}
.contact-left{left:141px;top:2440px;width:459px;height:422px;border-radius:40px 0 0 0;background:linear-gradient(135deg,#2bb9e2 0%,#26aee0 50%,#1d9fd6 100%)}
.contact-left h2{position:absolute;left:0;width:459px;top:152px;text-align:center;color:#fff;font-size:32px;line-height:48px;font-weight:500;letter-spacing:.5px}
.contact-left .btn{position:absolute;left:151px;top:280px;background:#fff;color:#333;padding:10px 21px}
.contact-right{left:600px;top:2440px;width:459px;height:422px;background:#fff;border:1px solid #ddd;border-left:none;border-radius:0 40px 0 0}
.field{position:absolute;left:59px;width:340px;height:42px;border:1px solid #bbb;border-radius:22px;font-size:13px;color:#555;padding:12px 18px}
.contact-right .submit{position:absolute;left:59px;top:324px;width:340px;height:42px;border-radius:22px;background:var(--cyan);color:#fff;font-size:15px;text-align:center;line-height:42px}

/* footer */
.footer .brand{left:142px;top:2955px}
.footer .about{left:142px;top:3025px;width:260px;font-size:14.5px;line-height:24px;color:#fff}
.fcol h4{font-size:16.5px;font-weight:500;color:#fff;letter-spacing:.3px}
.fcol ul{list-style:none;margin-top:18px;color:#fff}
.links li{font-size:13px;margin-bottom:21px}
.follow li{display:flex;align-items:center;gap:8px;font-size:15px;margin-bottom:13px}
.follow .c{width:28px;height:28px;border:1px solid #fff;border-radius:50%}
.contact li{position:relative;padding-left:30px;font-size:15px;line-height:21px;margin-bottom:7px}
.contact li b{display:block;font-weight:500}
.contact li svg{position:absolute;left:8px;top:4px}
.copyright{left:0;top:3235px;width:1200px;height:40px;background:var(--cyan);color:#fff;text-align:center;font-size:13px;line-height:40px}
</style>
</head>
<body>

<!-- Top bar -->
<div class="abs topbar">
  <div class="abs mail"><span class="dot-ic" style="display:flex;align-items:center;justify-content:center"><svg width="11" height="8" viewBox="0 0 11 8"><rect x=".5" y=".5" width="10" height="7" fill="none" stroke="#fff"/><path d="M.5.5l5 4 5-4" fill="none" stroke="#fff"/></svg></span>info@tbranwellconsulting.com</div>
  <div class="abs social">Visit Social Media Links:<span class="sq"></span><span class="sq"></span><span class="sq"></span><span class="sq"></span></div>
</div>

<!-- Header -->
<header class="abs header">
  <div class="abs brand">TBranwell</div>
  <nav class="abs nav"><a href="#">Home</a><a href="#">About Us</a><a href="#">Services</a></nav>
  <div class="abs callbox">
    <div class="ring"><svg width="24" height="24" viewBox="0 0 24 24"><path d="M6.6 10.8a15 15 0 006.6 6.6l2.2-2.2c.3-.3.7-.4 1-.2 1.1.4 2.3.6 3.6.6.6 0 1 .4 1 1V20c0 .6-.4 1-1 1A17 17 0 013 4c0-.6.4-1 1-1h3.5c.6 0 1 .4 1 1 0 1.3.2 2.5.6 3.6.1.3 0 .7-.2 1z" fill="#fff"/></svg></div>
    <div class="t">Call me today<br>(123) 456-7890</div>
  </div>
</header>

<!-- Hero -->
<section class="abs hero">
  <div class="abs hero-photo" role="img" aria-label="Two businesswomen reviewing work on a laptop at a bright office table with a model airplane"></div>
  <div class="abs kicker">Where Technology Meets Travel</div>
  <h1 class="abs">STRATEGIC CONSULTING<br>FOR THE FUTURE</h1>
  <div class="abs call">
    <div class="ring"><svg width="24" height="24" viewBox="0 0 24 24"><path d="M6.6 10.8a15 15 0 006.6 6.6l2.2-2.2c.3-.3.7-.4 1-.2 1.1.4 2.3.6 3.6.6.6 0 1 .4 1 1V20c0 .6-.4 1-1 1A17 17 0 013 4c0-.6.4-1 1-1h3.5c.6 0 1 .4 1 1 0 1.3.2 2.5.6 3.6.1.3 0 .7-.2 1z" fill="#111"/></svg></div>
    <div class="t">Call me today<br>(123) 456-7890</div>
  </div>
</section>

<!-- About -->
<section>
  <div class="abs about-bg"></div>
  <div class="abs about-frame"></div>
  <div class="abs about-photo" role="img" aria-label="Portrait of Rosalind Branwell in a dark blazer"></div>
  <div class="abs about-badge"><b>40</b><span>Year in<br>Travel Industry</span></div>
  <div class="abs about-text">
    <h2><em>About</em>ROSALIND BRANWELL</h2>
    <div class="role">Former Chief Information Officer, Bluecrest Airways<br>Harbor Pines, FL</div>
    <p style="margin-top:12px">Rosalind Branwell is a seasoned leader with a remarkable 40-year career in the travel industry, including 20 transformative years at Bluecrest Airways. As the Senior Vice President of Technology (CIO), Rosalind spearheaded some of the company's most significant technological and strategic transformations, helping Bluecrest Airways stay at the forefront of innovation in the competitive travel market. Her work bridged the gap between business strategy and technology, driving measurable success and resilience.</p>
    <p>With expertise in Leadership, Mentorship, Technology Strategy, and Digital Transformation, Rosalind is passionate about empowering IT leaders to forge stronger connections between their technology teams and business goals.</p>
    <a class="btn" href="#">Read More <span>↗</span></a>
  </div>
</section>

<!-- Services -->
<h2 class="abs section-title" style="top:1340px"><em>OUR</em> SERVICES</h2>

<article class="abs card" style="left:141px">
  <div class="img" role="img" aria-label="Hand moving a chess piece on a chessboard" style="background:linear-gradient(135deg,#e9e4dc,#8a6b4e 60%,#3a2c22)"></div>
  <div class="icon"><svg width="34" height="34" viewBox="0 0 34 34" fill="none" stroke="#fff" stroke-width="1.6"><rect x="12" y="4" width="18" height="12"/><circle cx="7" cy="9" r="3"/><path d="M3 22v-6h8l4-3"/><circle cx="10" cy="26" r="2"/><circle cx="18" cy="26" r="2"/><circle cx="26" cy="26" r="2"/><path d="M6 32a4 4 0 018 0M14 32a4 4 0 018 0M22 32a4 4 0 018 0"/></svg></div>
  <h3>Leadership Mentorship</h3>
  <ul style="top:212px"><li>Personalized coaching for IT leaders to develop strategic decision-making, emotional intelligence, and resilience.</li><li>Mentorship programs for aspiring technology leaders to...</li></ul>
  <a class="more" href="#">READ MORE <b>›</b></a>
</article>

<article class="abs card" style="left:459px">
  <div class="img" role="img" aria-label="Team presenting a strategy on a whiteboard in a modern office" style="background:linear-gradient(135deg,#1e3550,#49627e 50%,#c9d3dc)"></div>
  <div class="icon"><svg width="34" height="34" viewBox="0 0 34 34" fill="none" stroke="#fff" stroke-width="1.6"><circle cx="17" cy="13" r="9"/><circle cx="17" cy="13" r="4"/><path d="M17 2v3M17 21v3M6 13h3M25 13h3M12 26h10M13 30h8"/></svg></div>
  <h3>Technology Strategy Development</h3>
  <ul style="top:227px"><li>Creating IT strategies aligned with overall business goals.</li><li>Advising on IT infrastructure modernization and innovation.</li></ul>
  <a class="more" href="#">READ MORE <b>›</b></a>
</article>

<article class="abs card" style="left:777px">
  <div class="img" role="img" aria-label="Colleagues reviewing data on a tablet in an open office" style="background:linear-gradient(135deg,#2e2e2e,#6f7478 45%,#b7c0c4)"></div>
  <div class="icon"><svg width="34" height="34" viewBox="0 0 34 34" fill="none" stroke="#fff" stroke-width="1.6"><circle cx="17" cy="17" r="13"/><circle cx="14" cy="17" r="5"/><path d="M19 17h10M22 11h6M22 23h6"/><circle cx="29" cy="11" r="1.5"/><circle cx="29" cy="23" r="1.5"/></svg></div>
  <h3>Digital Transformation Consulting</h3>
  <ul style="top:227px;left:20px"><li>Assessing current digital maturity and identifying opportunities for improvement.</li><li>Designing and implementing digital...</li></ul>
  <a class="more" href="#">READ MORE <b>›</b></a>
</article>

<a class="abs btn" href="#" style="left:506px;top:1820px;width:187px;height:41px;justify-content:center">View All Services <span>↗</span></a>

<!-- Testimonials -->
<h2 class="abs section-title" style="top:1937px">TESTIMONIALS</h2>

<div class="abs arrow" style="left:65px;top:2125px;background:#fff;box-shadow:0 2px 8px rgba(0,0,0,.12)"><svg width="12" height="10" viewBox="0 0 12 10"><path d="M11 5H2M5 1L1 5l4 4" fill="none" stroke="#111" stroke-width="1.8"/></svg></div>

<article class="abs tcard active" style="left:141px">
  <div class="inner"></div>
  <p>Rosalind is a decisive and fair leader who exemplifies strength, wisdom, and empathy. She always possesses a clear vision for the future and is willing to make bold decisions which are grounded in data, expertise, and intuition while remaining open to diverse perspectives.<br><span style="display:block;margin-top:7px">Rosalind's leadership style fosters an inclusive environment where every voice matters,...</span></p>
  <div class="name">Daniel Hartley</div><div class="pos">CEO V4NQ</div>
  <div class="stars">★★★★★</div><div class="quote">”</div>
</article>
<div class="abs avatar" role="img" aria-label="Reviewer portrait" style="left:180px"></div>

<article class="abs tcard" style="left:628px">
  <p>Lorem ipsum dolor sit amet, consectetuer adipiscing elit, sed diam nonummy nibh euismod tincidunt ut laoreet dolore magna aliquam erat volutpat. Ut wisi enim ad minim veniam, quis nostrud exerci tation ullamcorper suscipit lobortis nisl ut aliquip ex ea commodo consequat.</p>
  <div class="name">Megan Foster</div><div class="pos">Lorem ipsum</div>
  <div class="stars">★★★★★</div><div class="quote">”</div>
</article>
<div class="abs avatar" role="img" aria-label="Reviewer portrait" style="left:667px"></div>

<div class="abs arrow" style="left:1089px;top:2125px;background:var(--cyan)"><svg width="12" height="10" viewBox="0 0 12 10"><path d="M1 5h9M7 1l4 4-4 4" fill="none" stroke="#fff" stroke-width="1.8"/></svg></div>

<div class="abs dots" style="left:0;top:2338px;width:1200px;height:14px">
  <span style="left:562px"></span>
  <span style="left:593px;background:radial-gradient(circle,var(--cyan) 40%,transparent 45%)"></span>
  <span style="left:622px"></span>
</div>

<!-- Contact + footer -->
<div class="abs footer-bg"></div>

<section class="abs contact-left" role="img" aria-label="Blue-tinted photo of an airplane in flight">
  <h2>TAILORED SOLUTIONS FOR<br>THE FUTURE OF TRAVEL</h2>
  <a class="btn" href="#">Get In Touch <span>↗</span></a>
</section>

<form class="abs contact-right">
  <div class="field" style="top:55px">First Name*</div>
  <div class="field" style="top:110px">Your Phone*</div>
  <div class="field" style="top:166px">Your Email*</div>
  <div class="field" style="top:222px;height:84px;border-radius:14px">Your Message</div>
  <div class="submit">Submit Now</div>
</form>

<footer class="footer">
  <div class="abs brand">TBranwell</div>
  <p class="abs about">Lorem ipsum dolor sit amet, consectetuer adipiscing elit, seed diam nonummy nibh euismod tincidunt utted.</p>

  <div class="abs fcol links" style="left:443px;top:2947px">
    <h4>QUICK LINKS</h4>
    <ul><li>• Home</li><li>• About Us</li><li>• Services</li></ul>
  </div>

  <div class="abs fcol follow" style="left:602px;top:2947px">
    <h4>FOLLOW US</h4>
    <ul style="margin-left:7px"><li><span class="c"></span>Network</li><li><span class="c"></span>Videos</li><li><span class="c"></span>Gallery</li><li><span class="c"></span>Updates</li></ul>
  </div>

  <div class="abs fcol contact" style="left:765px;top:2947px">
    <h4>CONTACT DETAILS</h4>
    <ul>
      <li><svg width="11" height="14" viewBox="0 0 11 14"><path d="M5.5 0A5.5 5.5 0 000 5.5C0 9.6 5.5 14 5.5 14S11 9.6 11 5.5A5.5 5.5 0 005.5 0zm0 7.5a2 2 0 110-4 2 2 0 010 4z" fill="#fff"/></svg><b>Address</b>123, Building Name, Street City,<br>State XY 123456</li>
      <li><svg width="13" height="13" viewBox="0 0 24 24"><path d="M6.6 10.8a15 15 0 006.6 6.6l2.2-2.2c.3-.3.7-.4 1-.2 1.1.4 2.3.6 3.6.6.6 0 1 .4 1 1V20c0 .6-.4 1-1 1A17 17 0 013 4c0-.6.4-1 1-1h3.5c.6 0 1 .4 1 1 0 1.3.2 2.5.6 3.6.1.3 0 .7-.2 1z" fill="#fff"/></svg><b>Phone</b>(123) 456-7890</li>
      <li><svg width="14" height="10" viewBox="0 0 14 10"><rect width="14" height="10" fill="#fff"/><path d="M0 0l7 5 7-5" fill="none" stroke="#1a1a1a"/></svg><b>Email</b>info@tbranwellconsulting.com</li>
    </ul>
  </div>

  <div class="abs copyright">Copyright © 2025 Rosalind Branwell Consulting. All Rights Reserved.</div>
</footer>

</body>
</html>
```